Exciting new aperitif brand needs a great label

Vel-Doro is a wonderful rich new premium-priced bitter aperitif, with a deep red colour, from a 100+ year old distillery (1890) near Turin in the Piedmont region of Italy. Inspired by Tessoli, it is perfectly formulated to elevate the classic Negroni cocktail (and variations on it). It also goes perfectly in a Spritz or a long mixed drink with soda or tonic. The name Vel-Doro is derived from the French for 'peak' and the Italian word for 'love'.

The label, which should take inspiration from Tessoli, but be distinctively different, can incoporate any number of premium label embellishments (foil, embossing, textures etc) and should be no greater than 11cm (height) x 9cm (width) with any core imagery restricted to a width of c.7cm.

The attached mood board should act as inspiration and colour should largely be restricted to reds, blues, whites and perhaps orange. For completeness, the label should note that the ABV is 25% and the bottle size 70cl.

Target Market(s)

21-45yr olds - equal split female/male

Colors
0054AA
0677BA
7BADD7
CADEEF
E8F1F8
0094D4
00A9DD
6FCCEA
C7EBF8
E9F6FB
EE7325
F08F49
F5BC92
FAE3D3
FDF4ED
EB3D1F
EC4F4E
F09395
F8D3D4
FCEDEE

Requirements
Must have
• Great lettering design on the name Vel-Doro

```html
<!DOCTYPE html>
<html lang="en">
<head>
<meta charset="utf-8">
<title>Vel-Doro Bitter Label</title>
<link rel="stylesheet" href="https://fonts.googleapis.com/css2?family=Limelight&family=Pinyon+Script&family=Roboto+Condensed:wght@700&display=swap">
<style>
  :root {
    --backdrop: #ececec;
    --label-white: #f7f5f2;
    --band-orange: #ee7325;
    --band-orange-light: #f08f49;
    --field-red: #d8262a;
    --banner-blue: #cadeef;
    --banner-blue-light: #e8f1f8;
    --name-navy: #0b3a9e;
    --foil-gold: #d6a84e;
    --emblem-tone: #f1e4e2;
    --copy-white: #ffffff;
  }
  html, body {
    margin: 0;
    padding: 0;
    width: 960px;
    height: 1200px;
    overflow: hidden;
    background: var(--backdrop);
  }
  .canvas {
    position: relative;
    width: 960px;
    height: 1200px;
  }
  .label {
    position: absolute;
    left: 165px;
    top: 70px;
    width: 630px;
    height: 1065px;
  }
  .since-line {
    font-family: "Roboto Condensed", sans-serif;
    font-weight: 700;
    font-size: 7px;
    letter-spacing: 1.2px;
    fill: var(--foil-gold);
  }
  .house-name {
    font-family: "Roboto Condensed", sans-serif;
    font-weight: 700;
    font-size: 7px;
    fill: var(--foil-gold);
  }
  .brand-name {
    font-family: "Limelight", serif;
    font-size: 72px;
    fill: var(--name-navy);
  }
  .style-word {
    font-family: "Pinyon Script", cursive;
    font-size: 46px;
    fill: var(--foil-gold);
  }
  .volume-copy {
    font-family: "Roboto Condensed", sans-serif;
    font-weight: 700;
    font-size: 11px;
    fill: var(--copy-white);
  }
</style>
</head>
<body>
<main class="canvas">
  <svg class="label" viewBox="-20 0 340 575" xmlns="http://www.w3.org/2000/svg">
    <polygon class="shield-outer" points="0,0 300,0 300,395 150,575 0,395" fill="var(--label-white)"/>
    <polygon class="shield-band" points="15,25 285,25 285,390 150,548 15,390" fill="var(--band-orange)"/>
    <polygon class="shield-band-inner" points="32,35 268,35 268,385 150,525 32,385" fill="var(--band-orange-light)"/>
    <polygon class="shield-field" points="42,42 258,42 258,382 150,510 42,382" fill="var(--field-red)"/>
    <polygon class="shield-dots" points="50,50 250,50 250,378 150,497 50,378" fill="none" stroke="var(--foil-gold)" stroke-width="1.4" stroke-dasharray="0.5 3" stroke-linecap="round"/>

    <text class="since-line" x="100" y="63" text-anchor="middle">SINCE</text>
    <g class="house-mark">
      <rect x="132" y="56" width="7" height="7" fill="var(--foil-gold)"/>
      <text class="house-name" x="142" y="63">Vel-Doro</text>
    </g>
    <text class="since-line" x="200" y="63" text-anchor="middle">1890</text>

    <rect class="name-banner" x="-14" y="92" width="328" height="136" rx="14" fill="var(--banner-blue)" stroke="var(--foil-gold)" stroke-width="2"/>
    <rect x="-8" y="98" width="316" height="124" rx="10" fill="var(--banner-blue-light)" opacity="0.55"/>
    <text class="brand-name" x="150" y="192" text-anchor="middle" textLength="290" lengthAdjust="spacingAndGlyphs">VEL-DORO</text>

    <text class="style-word" x="150" y="284" text-anchor="middle">Biter</text>

    <rect class="emblem-area" x="74" y="296" width="152" height="142" fill="var(--emblem-tone)" role="img" aria-label="Emblem illustration: heart formed by two white scallop shells with a domed tower rising through the centre"/>

    <text class="volume-copy" x="150" y="458" text-anchor="middle">ALC. 25%</text>
    <text class="volume-copy" x="150" y="472" text-anchor="middle">70 CL</text>
  </svg>
</main>
</body>
</html>
```